Website Redesign for a Restaurant with International Cuisine

We need a new website design for a Czech restaurant website that should be modern, simple, flexible, and mobile-friendly. We only need the PSD's, not the website coded.

-- Available images
https://files.quorbex.net/share/7XkPmq29LtWvRbZ4nHdYe8sJcAfU3oG1

-- Our current website
https://beta.vlnomirka.cz

-- Website we like
https://www.dubovaterasavelka.cz/en/
https://www.pelmorvane.com/

## Design following pages of our current website with given effort distribution:
-- 40% Home page, https://www.vlnomirka.cz/
-- 30% Regular Menu, https://www.vlnomirka.cz/stala_nabidka
-- 20% Contacts, https://www.vlnomirka.cz/kontakty
-- 10% About Us, https://www.vlnomirka.cz/o_nas

## Our strengths
-- Cozy, clean environment
-- we use KBFO Prime and KBFO Choice class meat
-- helpful, friendly staff
-- high quality traditional international cuisine (that is rare)
-- unique wood-fired oven
-- open parking space

## Our weaknesses
-- longer wait times (especially on weekends)
-- slightly expensive prices

Low design quality

Target Market(s)

People interested in gastronomy looking for high quality dishes.

Industry/Entity Type

Restaurant

Number of Pages Required

4 page

Font styles to use
Serif
Sans Serif

Colors

Designer to choose colors to be used in the design.

Requirements
Must have
• -- Preserve current content structure and the order of indiviual elements (use https://www.vlnomirka.cz).
• -- Emphasize both weekend events and daily deals. Weekend events are more of a priority.
• -- Also emphasize logo and the restaurant owner’s profile and the link to Trellon Plot.
• -- Mobile-friendly
• -- Use photos from our gallery to maximize authenticity:
• https://files.quorbex.net/share/7XkPmq29LtWvRbZ4nHdYe8sJcAfU3oG1
Nice to have
• -- Solutions with higher accessibility compliance (PLIX) are preferred.
• -- You may add important links/buttons or rephrase them if necessary.
Should not have
• -- Do not use photos from the current website. You may use externally sourced images if necessary.
• -- Do not use endless animations (carousels).
• -- Do not use embedded content (e.g. interactive map). You may or may not use a map as background decoration for that section.
• -- Nothing too crowded / busy.
• -- Not too many colors.

```html
<!DOCTYPE html>
<html lang="en">
<head>
<meta charset="utf-8">
<title>Vlnomirka – Fusion Restaurant</title>
<link rel="stylesheet" href="https://fonts.googleapis.com/css2?family=Cormorant+Garamond:ital,wght@0,400;0,500;0,600;1,400&family=Roboto:wght@300;400;500&display=swap">
<style>
:root{
  --red:#c8202a;
  --ink:#2a2a2a;
  --muted:#555;
  --white:#fff;
  --pale:#f1f1f1;
  --black:#111;
  --serif:'Cormorant Garamond', Georgia, serif;
  --sans:'Roboto', Arial, sans-serif;
}
*{box-sizing:border-box;margin:0;padding:0}
html,body{width:1200px;height:3846px;overflow:hidden}
body{position:relative;background:var(--white);font-family:var(--serif);color:var(--ink)}
.abs{position:absolute}
.sans{font-family:var(--sans)}

/* hero */
.hero{left:0;top:0;width:1200px;height:440px;background:linear-gradient(160deg,#3a3431 0%,#6b3a2e 35%,#8a4a34 50%,#3d3a36 75%,#22211f 100%)}
.nav-brand{left:228px;top:30px;color:#fff;font:400 17px var(--sans);letter-spacing:1px}
.nav-phone{left:804px;top:30px;color:#fff;font:400 17px var(--sans);display:flex;align-items:center;gap:8px}
.nav-menu{left:992px;top:33px}
.hero-title{left:0;top:145px;width:1200px;text-align:center;color:#fff;font:300 62px var(--sans)}

.brand-badge{left:490px;top:385px;width:220px;height:220px;border-radius:50%;background:#fff}
.brand-name{left:0;top:520px;width:1200px;text-align:center;font:600 44px var(--serif);color:var(--red);letter-spacing:2px;display:flex;justify-content:center;align-items:center;gap:14px}
.brand-dot{width:18px;height:18px;border-radius:50%;background:var(--red)}

/* owner */
.owner-text{left:180px;top:700px;width:360px;text-align:center}
.owner-name{font:400 44px var(--serif);color:var(--ink)}
.owner-role{margin-top:22px;font:italic 400 23px/1.35 var(--serif);color:var(--ink)}
.rule{width:26px;height:2px;background:var(--red);margin:18px auto}
.owner-bio{font:400 12px/1.4 var(--serif);color:var(--muted)}
.owner-bio em{color:var(--red);font-style:normal}
.owner-photo{left:596px;top:658px;width:500px;height:332px;background:linear-gradient(180deg,#d9ccb5 0%,#e8e4dc 45%,#cfd4d6 100%)}

/* quick tiles */
.tiles{left:132px;top:1066px;display:flex;gap:15px}
.tile{width:176px;height:116px;background:#fff;box-shadow:0 2px 8px rgba(0,0,0,.18);display:flex;flex-direction:column;align-items:center;justify-content:center;gap:18px}
.tile span{font:500 9px var(--sans);letter-spacing:.5px;color:var(--ink)}

/* about */
.about{left:0;top:1252px;width:1200px;height:464px;background:linear-gradient(100deg,#5d5650 0%,#3f3d3b 40%,#2d2b2a 70%,#4a3f3c 100%)}
.about-box{left:630px;top:1360px;width:450px;text-align:center;color:#fff}
.about-box h2{font:400 40px var(--serif)}
.about-box p{margin-top:20px;font:italic 400 21px/1.3 var(--serif);color:#eee}
.about-box .rule{margin:20px auto}
.btn-row{display:flex;gap:10px;justify-content:center}
.btn{background:#fff;color:var(--ink);font:500 9px var(--sans);letter-spacing:.4px;padding:7px 12px}
.btn.red{color:var(--red)}

/* menu */
.menu{left:0;top:1716px;width:1200px;height:1110px;background:linear-gradient(180deg,#ededec 0%,#f4f2f0 50%,#e6e4e2 100%)}
.menu-intro{left:200px;top:1830px;width:340px;text-align:center}
.menu-intro h2{font:400 40px var(--serif)}
.menu-intro p{margin-top:18px;font:italic 400 20px/1.3 var(--serif);color:var(--muted)}
.menu-tiles{left:172px;top:2050px;display:flex;gap:30px}
.menu-tiles .tile{width:122px;height:82px;gap:10px}
.card{background:#fff;box-shadow:0 3px 14px rgba(0,0,0,.18)}
.daily{left:600px;top:1788px;width:445px;height:402px;padding:40px 45px}
.weekend{left:170px;top:2216px;width:478px;height:540px;padding:48px 50px}
.card h3{font:400 32px/1.2 var(--serif);color:var(--ink)}
.card h3 b{font-weight:400;color:var(--red)}
.card .lead{margin-top:12px;font:italic 400 18px/1.35 var(--serif);color:var(--muted)}
.card .weekend-lead{text-align:center}
.dish{display:flex;justify-content:space-between;align-items:flex-end;margin-top:28px}
.dish-name{display:flex;align-items:center;gap:10px;font:500 15px var(--serif)}
.dish-desc{font:italic 400 11px/1.35 var(--serif);color:var(--muted);margin-left:26px;margin-top:6px;max-width:270px}
.price{font:500 15px var(--serif);white-space:nowrap}
.sizes{display:flex;gap:16px;text-align:left}
.sizes small{display:block;font:400 10px var(--serif);color:var(--muted)}

.quote-avatar{left:797px;top:2310px;width:150px;height:150px;border-radius:50%;background:radial-gradient(circle at 50% 40%,#d9a58c 0%,#b8836c 40%,#e2c03a 75%,#d0a91e 100%)}
.quote{left:700px;top:2500px;width:345px;text-align:center}
.quote p{font:italic 400 21px/1.3 var(--serif);color:var(--muted)}
.quote small{display:block;margin-top:6px;font:italic 400 11px var(--serif);color:var(--muted)}

/* contact */
.contact-sky{left:0;top:2826px;width:1200px;height:460px;background:linear-gradient(180deg,#1a5fb5 0%,#3a86d6 55%,#8fbde9 100%)}
.contact-photo{left:0;top:3286px;width:1200px;height:396px;background:linear-gradient(180deg,#e8ecef 0%,#cfd3d2 35%,#4e6b3c 62%,#3a3d3f 100%)}
.contact-intro{left:300px;top:2900px;width:600px;text-align:center;color:#fff}
.contact-intro h2{font:400 40px var(--serif)}
.contact-intro p{margin-top:16px;font:italic 400 21px/1.3 var(--serif)}
.contact-intro .rule{background:#fff;margin:18px auto}
.info{width:364px;height:172px;background:rgba(255,255,255,.9);text-align:center;padding:30px 30px}
.info h3{font:500 30px var(--serif)}
.info p{margin-top:12px;font:italic 400 17px/1.3 var(--serif);color:var(--muted)}
.open{left:128px;top:3450px}
.booking{left:712px;top:3450px}

/* footer */
.footer{left:0;top:3682px;width:1200px;height:164px;background:var(--black)}
.footer-badge{left:525px;top:3620px;width:150px;height:150px;border-radius:50%;background:var(--black)}
.footer-brand{left:0;top:3770px;width:1200px;text-align:center;color:#fff;font:600 32px var(--serif);letter-spacing:2px}
.footer-links{font:400 10px/1.9 var(--sans);color:#ddd;letter-spacing:.5px;list-style:none}
.fl-left{left:228px;top:3718px}
.fl-right{left:968px;top:3730px;text-align:left}
</style>
</head>
<body>

<header class="abs hero" role="img" aria-label="Photo: grilled sliced steak with herb sauce and peppercorns"></header>
<div class="abs nav-brand">VLNOMIRKA</div>
<div class="abs nav-phone">
  <svg width="16" height="16" viewBox="0 0 24 24" fill="#f0b43a"><path d="M6.6 10.8a15.5 15.5 0 0 0 6.6 6.6l2.2-2.2c.3-.3.7-.4 1-.2 1.1.4 2.3.6 3.6.6.6 0 1 .4 1 1V20c0 .6-.4 1-1 1A17 17 0 0 1 3 4c0-.6.4-1 1-1h3.5c.6 0 1 .4 1 1 0 1.3.2 2.5.6 3.6.1.3 0 .7-.2 1z"/></svg>
  +420 601 482 917
</div>
<svg class="abs nav-menu" width="18" height="14" viewBox="0 0 18 14" fill="#fff"><rect width="18" height="2"/><rect y="6" width="18" height="2"/><rect y="12" width="18" height="2"/></svg>
<h1 class="abs hero-title">Fusion Restaurant</h1>

<div class="abs brand-badge"></div>
<div class="abs brand-name"><span class="brand-dot"></span>VLNOMIRKA</div>

<section>
  <div class="abs owner-text">
    <h2 class="owner-name">Radovan Kletečka</h2>
    <p class="owner-role">Owner and Chef and a recognized Grilling and Broiling Expert</p>
    <div class="rule"></div>
    <p class="owner-bio">Member and certified commissioner of <em>SKK (Czech)</em>, member of <em>HRS ČR (Czech)</em> and its gastronomy section. <em>Restaurateur of the Year 2007 (Czech)</em> and <em>nominated in 2008 (Czech)</em>. Winner of the Bronze Medal of <em>W.O. Feldberg (Czech)</em>.</p>
  </div>
  <div class="abs owner-photo" role="img" aria-label="Photo: the chef in white jacket standing at the bar"></div>
</section>

<nav class="abs tiles">
  <div class="tile">
    <svg width="40" height="44" viewBox="0 0 40 44" fill="var(--red)"><path d="M4 2h3v12h2V2h3v12h2V2h3v14a5 5 0 0 1-4 5v21h-5V21a5 5 0 0 1-4-5z"/><path d="M26 2c6 0 9 8 9 16v6h-4v18h-5z"/></svg>
    <span>DAILY OFFER</span>
  </div>
  <div class="tile">
    <svg width="40" height="42" viewBox="0 0 40 42" fill="var(--red)"><rect x="9" y="1" width="4" height="8"/><rect x="27" y="1" width="4" height="8"/><path d="M3 5h36v36H3zM7 15v22h28V15z"/><path d="M12 26l3-3 4 4 8-8 3 3-11 11z"/></svg>
    <span>WEEKEND EVENTS</span>
  </div>
  <div class="tile">
    <svg width="36" height="42" viewBox="0 0 36 42" fill="var(--red)"><path d="M2 4h10a6 6 0 0 1 12 0h10v38H2z"/><g fill="#fff"><circle cx="10" cy="16" r="2"/><rect x="15" y="15" width="13" height="2"/><circle cx="10" cy="24" r="2"/><rect x="15" y="23" width="13" height="2"/><circle cx="10" cy="32" r="2"/><rect x="15" y="31" width="13" height="2"/></g></svg>
    <span>REGULAR MENU</span>
  </div>
  <div class="tile">
    <svg width="46" height="40" viewBox="0 0 46 40" fill="var(--red)"><path d="M1 8l12-5 10 5 12-5 10 5v30l-10-4-12 5-10-5-12 5z" opacity=".85"/><path d="M23 4a9 9 0 0 1 9 9c0 7-9 17-9 17s-9-10-9-17a9 9 0 0 1 9-9z" fill="#9c1820"/><circle cx="23" cy="13" r="3" fill="#fff"/></svg>
    <span>WHERE TO FIND US</span>
  </div>
  <div class="tile">
    <svg width="40" height="40" viewBox="0 0 40 40"><rect width="40" height="40" rx="3" fill="#3b5998"/></svg>
    <span>CHATTERLY (CZECH)</span>
  </div>
</nav>

<section>
  <div class="abs about" role="img" aria-label="Photo: covered restaurant terrace with tables and chairs"></div>
  <div class="abs about-box">
    <h2>About Us</h2>
    <p>Since 2005, our unique Czech restaurant concept has filled the gap between all the fast food restaurants and expensive so-called luxury restaurants.</p>
    <div class="rule"></div>
    <div class="btn-row">
      <span class="btn red">&#9906; VIRTUAL TOUR</span>
      <span class="btn">RESTAURANT CONCEPT</span>
      <span class="btn">OUR STEAKS</span>
      <span class="btn">VIDEO ARCHIVES</span>
    </div>
  </div>
</section>

<section>
  <div class="abs menu" role="img" aria-label="Faded photo of the dining room"></div>
  <div class="abs menu-intro">
    <h2>Menu</h2>
    <p>We make international dishes according to traditional recipes as people all over the world enjoy them.</p>
    <div class="rule"></div>
  </div>
  <div class="abs menu-tiles">
    <div class="tile">
      <svg width="26" height="30" viewBox="0 0 36 42" fill="var(--red)"><path d="M2 4h10a6 6 0 0 1 12 0h10v38H2z"/><g fill="#fff"><rect x="9" y="15" width="18" height="2"/><rect x="9" y="23" width="18" height="2"/><rect x="9" y="31" width="18" height="2"/></g></svg>
      <span>REGULAR MENU</span>
    </div>
    <div class="tile">
      <svg width="32" height="26" viewBox="0 0 32 26" fill="var(--red)"><path d="M2 6h22v10a8 8 0 0 1-8 8h-6a8 8 0 0 1-8-8z"/><path d="M24 8h3a4 4 0 0 1 0 8h-3v-3h3a1 1 0 0 0 0-2h-3z"/><rect x="8" y="0" width="2" height="4"/><rect x="14" y="0" width="2" height="4"/></svg>
      <span>DRINK LIST</span>
    </div>
    <div class="tile">
      <svg width="20" height="32" viewBox="0 0 20 32" fill="var(--red)"><path d="M2 1h16c1 8-1 14-7 15v11h5v3H4v-3h5V16C3 15 1 9 2 1z"/></svg>
      <span>WINE LIST</span>
    </div>
  </div>

  <article class="abs card daily">
    <h3><b>Daily Offer</b>, November 15, 2018</h3>
    <p class="lead" style="text-align:center">We cook a lunch menu every weekday using fresh local ingredients.</p>
    <div class="dish">
      <div>
        <div class="dish-name"><svg width="14" height="12" viewBox="0 0 14 12"><path d="M1 4h12a6 6 0 0 1-12 0z" fill="var(--ink)"/></svg>Potato soup</div>
        <div class="dish-desc">With forest mushrooms</div>
      </div>
      <div class="sizes"><div class="price"><small>small</small>CZK 49</div><div class="price"><small>large</small>CZK 55</div></div>
    </div>
    <div class="dish">
      <div>
        <div class="dish-name"><svg width="14" height="12" viewBox="0 0 14 12"><path d="M1 4h12a6 6 0 0 1-12 0z" fill="var(--ink)"/></svg>Mushroom veal stew</div>
        <div class="dish-desc">Stewed veal in delicate cream sauce with forest mushrooms and homemade bread dumplings</div>
      </div>
      <div class="price">CZK 179</div>
    </div>
  </article>

  <article class="abs card weekend">
    <h3 style="text-align:center"><b>Weekend special</b> including Friday evening, November 2–4, 2018</h3>
    <p class="lead weekend-lead">On weekends, we mostly offer dishes made in an oven, grilled and broiled over wood.</p>
    <div class="dish">
      <div>
        <div class="dish-name"><svg width="14" height="12" viewBox="0 0 14 12"><path d="M1 4h12a6 6 0 0 1-12 0z" fill="var(--ink)"/></svg>Homemade sirloin steak tartare, 50 g</div>
        <div class="dish-desc">Pre-mixed, garlic toast</div>
      </div>
      <div class="price">CZK 129</div>
    </div>
    <div class="dish">
      <div>
        <div class="dish-name"><svg width="14" height="12" viewBox="0 0 14 12"><path d="M1 4h12a6 6 0 0 1-12 0z" fill="var(--ink)"/></svg>Beef sirloin in cream sauce</div>
        <div class="dish-desc">Marinated rump, homemade bread dumplings, lemon, lingonberries</div>
      </div>
      <div class="price">CZK 209</div>
    </div>
    <div class="dish">
      <div>
        <div class="dish-name"><svg width="14" height="12" viewBox="0 0 14 12"><path d="M1 4h12a6 6 0 0 1-12 0z" fill="var(--ink)"/></svg>Homemade sirloin steak tartare, 150 g</div>
        <div class="dish-desc">Pre-mixed, garlic toast</div>
      </div>
      <div class="price">CZK 289</div>
    </div>
  </article>

  <div class="abs quote-avatar" role="img" aria-label="Portrait photo of the concept founder"></div>
  <blockquote class="abs quote">
    <p>Give people what they want and what they deserve for their money.</p>
    <small>— M. D. Oravec, Founder of the VLNOMIRKA Concept</small>
    <svg style="margin-top:14px" width="32" height="26" viewBox="0 0 32 26" fill="var(--red)"><path d="M2 2h12v12l-6 10H3l5-10H2zM18 2h12v12l-6 10h-5l5-10h-6z"/></svg>
  </blockquote>
</section>

<section>
  <div class="abs contact-sky"></div>
  <div class="abs contact-photo" role="img" aria-label="Photo: restaurant building with terrace and hedge under blue sky"></div>
  <div class="abs contact-intro">
    <h2>Contact</h2>
    <p>The restaurant is situated right next to the D12 highway intersection to the city of Lipnice nad Brodem and Dolní Kamenec (Exit 29).</p>
    <div class="rule"></div>
    <div class="btn-row">
      <span class="btn">SUBSCRIBE TO OUR NEWSLETTER</span>
      <span class="btn">CONTACT FORM</span>
      <span class="btn">FREQUENTLY ASKED QUESTIONS</span>
    </div>
  </div>
  <div class="abs info open">
    <h3>Open Daily</h3>
    <p>Open daily from 11 am to 10 pm, Fridays and Saturdays until 11 pm</p>
  </div>
  <div class="abs info booking">
    <h3>Booking</h3>
    <p>Bookings are accepted only by telephone at +420 601 482 917.</p>
  </div>
</section>

<footer>
  <div class="abs footer"></div>
  <div class="abs footer-badge"></div>
  <div class="abs footer-brand">VLNOMIRKA</div>
  <ul class="abs footer-links fl-left"><li>CHATTERLY</li><li>PLUSRING</li><li>TRIPVANE</li><li>SQUARESTOP</li></ul>
  <ul class="abs footer-links fl-right"><li>ABOUT US</li><li>MENU</li><li>CONTACT</li></ul>
</footer>

</body>
</html>
```